Firma Rusow Innenausbau
Zielgruppe
Wir bieten unserem Kunden den gesamten Innenausbau an. Böden, Wände, Decken, Trockenbau Türen, Speziell auch Spanndecken siehe auch www.rusow-Innenausbau.de
Zielgruppe sind Privatleute sowie Bauunternehmer und Bauträger.
Aufgabenstellung
Die Visitenkarten sollen unseren modernen Stil wie auf der HP sowie auf unseren Autos haben.

```html
<!DOCTYPE html>
<html lang="de">
<head>
<meta charset="utf-8">
<title>Rusow Innenausbau – Geschäftsausstattung</title>
<link rel="stylesheet" href="https://fonts.googleapis.com/css2?family=Open+Sans:wght@400;600;700&display=swap">
<style>
:root{
  --stage:#4a4a4a;
  --paper:#ffffff;
  --orange:#e35f0c;
  --brown:#6b2b0e;
  --ink:#555555;
  --muted:#8a8a8a;
  --rule:#d8d8d8;
  --dim:#ffffff;
  --pink:#e84fa8;
}
*{box-sizing:border-box;margin:0;padding:0}
html,body{width:1200px;height:1197px;overflow:hidden;background:var(--stage);font-family:"Open Sans",Arial,sans-serif}
.canvas{position:relative;width:1200px;height:1197px}
.abs{position:absolute}
.dimension{position:absolute;overflow:visible}
.dim-label{position:absolute;color:var(--dim);font-size:13px;white-space:nowrap}
.dim-label.vertical{transform:rotate(-90deg);transform-origin:center}
.dim-label.vertical-r{transform:rotate(90deg);transform-origin:center}
.sheet{position:absolute;background:var(--paper);box-shadow:0 4px 10px rgba(0,0,0,.45);overflow:hidden}
.brand{position:absolute;display:flex;align-items:center;gap:6px;color:var(--ink);font-weight:600;white-space:nowrap}
.brand .mark{background:var(--orange);display:inline-block}
.band{position:absolute;left:0;right:0;bottom:0}
.band > svg{position:absolute;inset:0;display:block}
.band .url{position:absolute;left:0;right:0;top:0;bottom:0;display:flex;align-items:center;justify-content:center;gap:4px;color:#fff;font-weight:700;white-space:nowrap}
.band .url svg{flex:none;display:block}
.contact-line{position:absolute;display:flex;gap:6px;align-items:flex-start;color:var(--muted);line-height:1.35;white-space:nowrap}
.contact-line svg{flex:none}
.photo{position:absolute}
.services{position:absolute;color:var(--ink);font-size:11.5px;line-height:15px;white-space:nowrap}
.services h3{color:var(--orange);font-size:14px;font-weight:700;line-height:17px}
.services li{list-style:none}
.services li::before{content:"★";color:var(--orange);margin-right:4px}
.card-url{position:absolute;left:0;right:0;display:flex;justify-content:center;align-items:center;gap:5px;color:#fff;font-weight:700;font-size:14px}
</style>
</head>
<body>
<div class="canvas">

  <!-- Dimension lines -->
  <svg class="dimension" style="left:0;top:0" width="1200" height="1197">
    <g stroke="#2f2f2f" stroke-width="1">
      <line x1="105" y1="50" x2="105" y2="88"/><line x1="608" y1="50" x2="608" y2="88"/>
      <line x1="59" y1="96" x2="100" y2="96"/><line x1="59" y1="809" x2="100" y2="809"/>
      <line x1="105" y1="824" x2="105" y2="855"/><line x1="608" y1="824" x2="608" y2="855"/>
      <line x1="624" y1="96" x2="655" y2="96"/><line x1="624" y1="809" x2="655" y2="809"/>
    </g>
    <g stroke="var(--dim)" stroke-width="1.5" fill="var(--dim)">
      <line x1="110" y1="75" x2="603" y2="75"/>
      <polygon points="106,75 122,68 118,75 122,82"/><polygon points="607,75 591,68 595,75 591,82"/>
      <line x1="89" y1="100" x2="89" y2="805"/>
      <polygon points="89,96 82,114 89,109 96,114"/><polygon points="89,809 82,791 89,796 96,791"/>
      <line x1="710" y1="506" x2="1075" y2="506"/>
      <polygon points="705,506 721,499 717,506 721,513"/><polygon points="1079,506 1063,499 1067,506 1063,513"/>
      <line x1="1105" y1="532" x2="1105" y2="768"/>
      <polygon points="1105,528 1098,544 1105,540 1112,544"/><polygon points="1105,772 1098,756 1105,760 1112,756"/>
      <line x1="166" y1="874" x2="533" y2="874"/>
      <polygon points="162,874 178,867 174,874 178,881"/><polygon points="537,874 521,867 525,874 521,881"/>
      <line x1="564" y1="900" x2="564" y2="1134"/>
      <polygon points="564,896 557,912 564,908 571,912"/><polygon points="564,1138 557,1122 564,1126 571,1122"/>
      <line x1="720" y1="874" x2="1087" y2="874"/>
      <polygon points="716,874 732,867 728,874 732,881"/><polygon points="1091,874 1075,867 1079,874 1075,881"/>
      <line x1="1117" y1="900" x2="1117" y2="1134"/>
      <polygon points="1117,896 1110,912 1117,908 1124,912"/><polygon points="1117,1138 1110,1122 1117,1126 1124,1122"/>
    </g>
  </svg>
  <div class="dim-label" style="left:329px;top:56px">210 mm.</div>
  <div class="dim-label vertical" style="left:34px;top:434px">297 mm.</div>
  <div class="dim-label" style="left:843px;top:488px">85 mm.</div>
  <div class="dim-label vertical-r" style="left:1088px;top:661px">55 mm.</div>
  <div class="dim-label" style="left:302px;top:856px">85 mm.</div>
  <div class="dim-label vertical-r" style="left:547px;top:1028px">55 mm.</div>
  <div class="dim-label" style="left:855px;top:856px">85 mm.</div>
  <div class="dim-label vertical-r" style="left:1100px;top:1028px">55 mm.</div>

  <!-- Letterhead -->
  <section class="sheet letterhead" style="left:105px;top:96px;width:503px;height:713px">
    <div class="brand" style="left:51px;top:44px;font-size:19px">
      <span class="mark" style="width:12px;height:12px"></span>Rusow Innenausbau
    </div>

    <div class="abs" style="left:353px;top:27px;width:1px;height:184px;background:var(--rule)"></div>

    <div class="contact-line" style="left:361px;top:27px;font-size:7px">
      <svg width="10" height="10" viewBox="0 0 10 10"><path d="M5 0.5C3 0.5 1.6 2 1.6 3.8 1.6 6.2 5 9.5 5 9.5S8.4 6.2 8.4 3.8C8.4 2 7 .5 5 .5Z" fill="var(--brown)"/><circle cx="5" cy="3.8" r="1.3" fill="#fff"/></svg>
      <span>Lindenhofweg, 12<br>52349 Dürenfeld</span>
    </div>
    <div class="contact-line" style="left:361px;top:50px;font-size:7px">
      <svg width="10" height="10" viewBox="0 0 10 10"><circle cx="5" cy="5" r="4.3" fill="none" stroke="var(--orange)" stroke-width="1"/><path d="M3.5 2.8c-.6.8 0 2.6 1.1 3.7s2 1.5 2.4 1l-.9-1-.8.4c-.4-.3-1-1-1.2-1.5l.5-.7Z" fill="var(--orange)"/></svg>
      <span>0 21 45 / 38 60 512</span>
    </div>
    <div class="contact-line" style="left:361px;top:68px;font-size:7px">
      <svg width="11" height="9" viewBox="0 0 11 9"><rect x=".5" y=".5" width="10" height="8" fill="var(--orange)"/><path d="M.5 .5 5.5 5 10.5 .5" fill="none" stroke="#fff" stroke-width="1"/></svg>
      <span>kontakt@raum-werk.de</span>
    </div>
    <div class="abs" style="left:360px;top:87px;color:var(--orange);font-size:7px;font-weight:600">Konto</div>
    <div class="abs" style="left:360px;top:96px;color:var(--muted);font-size:5px;line-height:7px;white-space:nowrap">
      Kreiskasse Dürenfeld<br>(BLZ 0000XXXX), Kto.-Nr. 4417023<br><span style="display:block;height:3px"></span>IBAN DE00XXXX000000000000XX<br>SWIFT-BIC KRDFDEXXXXX
    </div>

    <svg class="abs" style="left:52px;top:109px" width="211" height="103" viewBox="0 0 211 103">
      <g fill="none" stroke="#888" stroke-width="1">
        <path d="M0.5 14V8Q.5 .5 8 .5H16"/><path d="M195 .5H203Q210.5 .5 210.5 8V14"/>
        <path d="M0.5 89V95Q.5 102.5 8 102.5H16"/><path d="M195 102.5H203Q210.5 102.5 210.5 95V89"/>
      </g>
    </svg>
    <div class="abs" style="left:69px;top:155px;color:var(--ink);font-size:7.5px;line-height:10px">Herr.:<br>Heiner Brockmann<br>Web Master<br>City</div>

    <div class="abs" style="left:1px;top:253px;width:17px;height:1px;background:var(--rule)"></div>
    <div class="abs" style="left:1px;top:491px;width:17px;height:1px;background:var(--rule)"></div>

    <div class="band" style="height:19px">
      <svg width="503" height="19" viewBox="0 0 503 19">
        <rect width="503" height="19" fill="var(--orange)"/>
        <polygon points="420,0 503,0 503,19 402,19" fill="var(--brown)"/>
        <polygon points="385,19 395,19 407,0 397,0" fill="#f3d5c0"/>
        <polygon points="398,19 406,19 418,0 410,0" fill="#c9a48b"/>
      </svg>
      <div class="url" style="font-size:8.5px;padding-right:20px">
        <svg width="9" height="9" viewBox="0 0 10 10"><g fill="none" stroke="#fff" stroke-width=".9"><circle cx="5" cy="5" r="4.3"/><ellipse cx="5" cy="5" rx="2" ry="4.3"/><line x1=".7" y1="5" x2="9.3" y2="5"/></g></svg>
        rusow-innenausbau.de
      </div>
    </div>
  </section>

  <!-- Envelope -->
  <section class="envelope abs" style="left:626px;top:93px;width:557px;height:358px">
    <svg class="abs" style="left:0;top:0" width="557" height="80" viewBox="0 0 557 80">
      <path d="M0 78 L24 10 Q28 0 38 0 H522 Q532 0 536 10 L557 78Z" fill="var(--paper)"/>
    </svg>
    <div class="sheet" style="left:0;top:78px;width:557px;height:280px">
      <div class="brand" style="left:56px;top:54px;font-size:19px">
        <span class="mark" style="width:12px;height:12px"></span>Rusow Innenausbau
      </div>
      <div class="abs" style="left:51px;top:126px;width:228px;height:114px;border:1px solid var(--pink);border-radius:8px"></div>
      <div class="abs" style="left:55px;top:130px;width:220px;height:106px;border:1px dashed #999;border-radius:6px"></div>
      <div class="photo" role="img" aria-label="Foto eines lächelnden Handwerkers mit Spachtel, Daumen hoch, mit Schriftzug Kreativ, individuell &amp; effizient!" style="left:296px;top:0;width:261px;height:261px;background:linear-gradient(90deg,#ffffff 0%,#ececec 35%,#d9d9d9 70%,#c9c9c9 100%)"></div>
      <div class="band" style="height:19px">
        <svg width="557" height="19" viewBox="0 0 557 19">
          <rect width="557" height="19" fill="var(--orange)"/>
          <polygon points="470,0 557,0 557,19 458,19" fill="var(--brown)"/>
          <polygon points="432,19 441,19 453,0 444,0" fill="#f3d5c0"/>
          <polygon points="445,19 453,19 465,0 457,0" fill="#c9a48b"/>
        </svg>
        <div class="url" style="font-size:8.5px;padding-right:100px">
          <svg width="9" height="9" viewBox="0 0 10 10"><g fill="none" stroke="#fff" stroke-width=".9"><circle cx="5" cy="5" r="4.3"/><ellipse cx="5" cy="5" rx="2" ry="4.3"/><line x1=".7" y1="5" x2="9.3" y2="5"/></g></svg>
          rusow-innenausbau.de
        </div>
      </div>
    </div>
  </section>

  <!-- Business card front -->
  <section class="sheet card-front" style="left:697px;top:530px;width:380px;height:245px">
    <div class="abs" style="left:0;top:0;width:380px;height:11px;background:var(--brown)"></div>
    <div class="photo" role="img" aria-label="Foto eines lächelnden Handwerkers mit Spachtel, Daumen hoch, mit Schriftzug Kreativ, individuell &amp; effizient!" style="left:218px;top:11px;width:162px;height:214px;background:linear-gradient(90deg,#ffffff 0%,#ececec 35%,#d6d6d6 75%,#c8c8c8 100%)"></div>
    <div class="abs" style="left:18px;top:56px;width:16px;height:16px;background:var(--orange)"></div>
    <div class="brand" style="left:17px;top:78px;font-size:26px;line-height:27px;display:block;font-weight:600">Rusow<br>Innenausbau</div>

    <div class="contact-line" style="left:23px;top:156px;font-size:8.5px">
      <svg width="12" height="12" viewBox="0 0 10 10"><path d="M5 0.5C3 0.5 1.6 2 1.6 3.8 1.6 6.2 5 9.5 5 9.5S8.4 6.2 8.4 3.8C8.4 2 7 .5 5 .5Z" fill="var(--brown)"/><circle cx="5" cy="3.8" r="1.3" fill="#fff"/></svg>
      <span>Lindenhofweg, 12<br>52349 Dürenfeld</span>
    </div>
    <div class="contact-line" style="left:23px;top:185px;font-size:8.5px">
      <svg width="12" height="12" viewBox="0 0 10 10"><circle cx="5" cy="5" r="4.3" fill="none" stroke="var(--orange)" stroke-width="1"/><path d="M3.5 2.8c-.6.8 0 2.6 1.1 3.7s2 1.5 2.4 1l-.9-1-.8.4c-.4-.3-1-1-1.2-1.5l.5-.7Z" fill="var(--orange)"/></svg>
      <span>0 21 45 / 38 60 512</span>
    </div>
    <div class="contact-line" style="left:23px;top:201px;font-size:8.5px">
      <svg width="12" height="12" viewBox="0 0 12 12"><rect x="3" y=".8" width="6" height="10.4" rx="1" fill="none" stroke="var(--orange)" stroke-width="1"/><line x1="5" y1="9.5" x2="7" y2="9.5" stroke="var(--orange)"/></svg>
      <span>0160 / 48 37 20 19</span>
    </div>

    <div class="band" style="height:20px">
      <svg width="380" height="20" viewBox="0 0 380 20">
        <rect width="380" height="20" fill="var(--orange)"/>
        <polygon points="293,0 380,0 380,20 280,20" fill="var(--brown)"/>
        <polygon points="256,20 265,20 277,0 268,0" fill="#f3d5c0"/>
        <polygon points="269,20 277,20 289,0 281,0" fill="#c9a48b"/>
      </svg>
      <div class="url" style="font-size:10px;font-weight:400;justify-content:flex-start;padding-left:27px;gap:6px">
        <svg width="12" height="10" viewBox="0 0 11 9"><rect x=".5" y=".5" width="10" height="8" fill="#fff"/><path d="M.5 .5 5.5 5 10.5 .5" fill="none" stroke="var(--orange)" stroke-width="1"/></svg>
        kontakt@raum-werk.de
      </div>
    </div>
  </section>

  <!-- Business card back, variant A -->
  <section class="sheet card-back" style="left:160px;top:897px;width:380px;height:246px;background:linear-gradient(135deg,#d4d4d4,#c2c2c2 50%,#cfcfcf)">
    <div class="photo" role="img" aria-label="Orangefarbener Pinselstrich mit Glättkelle" style="left:2px;top:6px;width:198px;height:205px;background:radial-gradient(ellipse at 55% 30%,rgba(232,110,40,.85),rgba(232,110,40,.35) 55%,rgba(232,110,40,0) 75%)"></div>
    <div class="services" style="left:215px;top:36px">
      <h3>Spanndecken</h3>
      <ul><li>10 Jahre Herstellergarantie</li><li>Einbau an nur einen Tag</li><li>Pflegeleichtes Material</li><li>Badezimmer geeignet</li><li>Decke muss nie mehr</li></ul>
      <div>gestrichen werden</div>
    </div>
    <div class="services" style="left:63px;top:98px">
      <h3>Trockenbau</h3>
      <ul><li>Trennwände</li><li>Abgehängte Decken</li><li>Brandschutz</li><li>Türen Bauelemente</li><li>Mineralfasrdecken</li></ul>
    </div>
    <svg class="abs" style="left:0;top:190px" width="380" height="56" viewBox="0 0 380 56"><path d="M0 56 Q190 -30 380 56Z" fill="var(--brown)"/></svg>
    <div class="card-url" style="top:214px">
      <svg width="14" height="14" viewBox="0 0 10 10"><g fill="none" stroke="#fff" stroke-width=".8"><circle cx="5" cy="5" r="4.3"/><ellipse cx="5" cy="5" rx="2" ry="4.3"/><line x1=".7" y1="5" x2="9.3" y2="5"/></g></svg>
      rusow-innenausbau.de
    </div>
  </section>

  <!-- Business card back, variant B -->
  <section class="sheet card-back" style="left:714px;top:897px;width:380px;height:246px;background:linear-gradient(135deg,#d4d4d4,#c2c2c2 50%,#cfcfcf)">
    <div class="photo" role="img" aria-label="Orangefarbener Pinselstrich mit Glättkelle" style="left:2px;top:6px;width:198px;height:205px;background:radial-gradient(ellipse at 55% 30%,rgba(232,110,40,.85),rgba(232,110,40,.35) 55%,rgba(232,110,40,0) 75%)"></div>
    <div class="services" style="left:215px;top:36px">
      <h3>Spanndecken</h3>
      <ul><li>10 Jahre Herstellergarantie</li><li>Einbau an nur einen Tag</li><li>Pflegeleichtes Material</li><li>Badezimmer geeignet</li><li>Decke muss nie mehr</li></ul>
      <div>gestrichen werden</div>
    </div>
    <div class="services" style="left:63px;top:98px">
      <h3>Trockenbau</h3>
      <ul><li>Trennwände</li><li>Abgehängte Decken</li><li>Brandschutz</li><li>Türen Bauelemente</li><li>Mineralfasrdecken</li></ul>
    </div>
    <div class="brand" style="left:302px;top:170px;font-size:12px;color:var(--brown);font-weight:700">
      <span class="mark" style="width:8px;height:8px"></span>Rusow
    </div>
    <svg class="abs" style="left:0;top:190px" width="380" height="56" viewBox="0 0 380 56"><path d="M0 56 Q190 -30 380 56Z" fill="var(--brown)"/></svg>
    <div class="card-url" style="top:214px">
      <svg width="14" height="14" viewBox="0 0 10 10"><g fill="none" stroke="#fff" stroke-width=".8"><circle cx="5" cy="5" r="4.3"/><ellipse cx="5" cy="5" rx="2" ry="4.3"/><line x1=".7" y1="5" x2="9.3" y2="5"/></g></svg>
      rusow-innenausbau.de
    </div>
  </section>

</div>
</body>
</html>
```